Long term design collaboration - mobile app design & web app design

We are looking for a talented mobile designer to help us improve our UI & UX for mobile app and web app.

The screens that need to be redesigned are attached.

There is potentially a lot more work in future design available for the successful candidate.
The successful candidate would have to take part in daily stand-up around 3 times per week.
The successful candidate would join a dev team
We are software company that does property management

```html
<!DOCTYPE html>
<html lang="en">
<head>
<meta charset="utf-8">
<title>Keyvale – Property Management App Screens</title>
<link rel="stylesheet" href="https://fonts.googleapis.com/css2?family=Poppins:wght@400;500;600;700&display=swap">
<style>
:root{
  --blue:#1d7fdb;
  --blue-dark:#0f5fb3;
  --blue-soft:#e7f1fc;
  --teal:#1fb89a;
  --bg:#ffffff;
  --panel:#f3f7fc;
  --ink:#17273a;
  --muted:#7b8a9c;
  --line:#e1e8f0;
  --green:#27b36a;
  --red:#e0524a;
  --amber:#f2a33a;
  --frame:#1a1f29;
}
*{box-sizing:border-box;margin:0;padding:0}
html,body{width:755px;height:1200px;overflow:hidden;background:var(--bg)}
body{position:relative;font-family:"Poppins",Arial,sans-serif;color:var(--ink)}
.abs{position:absolute}

/* section labels */
.label{position:absolute;font-size:6.5px;font-weight:600;letter-spacing:.08em;color:var(--ink);text-transform:uppercase}

/* ---------- desktop screen ---------- */
.desk{position:absolute;width:472px;height:226px;border:2px solid var(--blue);border-radius:6px;background:var(--panel);overflow:hidden;display:flex}
.side{width:78px;background:linear-gradient(180deg,var(--blue),var(--blue-dark));color:#fff;padding:8px 7px;display:flex;flex-direction:column;gap:3px;font-size:5.5px}
.brand{display:flex;align-items:center;gap:4px;font-size:8px;font-weight:600;margin-bottom:6px}
.brand i{width:9px;height:9px;background:#fff;border-radius:2px;display:block}
.side .search{background:rgba(255,255,255,.22);border-radius:8px;height:11px;margin-bottom:5px;padding:2px 6px;font-size:5px}
.nav{padding:3px 5px;border-radius:4px;display:flex;align-items:center;gap:4px}
.nav::before{content:"";width:5px;height:5px;border-radius:1px;border:1px solid #fff;opacity:.85}
.nav.on{background:rgba(255,255,255,.25)}
.side .out{margin-top:auto;opacity:.85}
.main{flex:1;display:flex;flex-direction:column}
.top{height:26px;background:#fff;display:flex;align-items:center;justify-content:space-between;padding:0 10px;border-bottom:1px solid var(--line)}
.top h1{font-size:9px;font-weight:600}
.user{display:flex;align-items:center;gap:4px;font-size:5.5px}
.user i{width:11px;height:11px;border-radius:50%;background:var(--blue-soft);border:1px solid var(--blue);display:block}
.body{flex:1;display:flex;gap:6px;padding:7px}
.col{display:flex;flex-direction:column;gap:6px}
.col.left{width:250px}
.col.right{flex:1}
.stats{display:flex;gap:6px}
.stat{flex:1;height:40px;border-radius:5px;color:#fff;padding:6px 7px;font-size:5px}
.stat b{display:block;font-size:9px;font-weight:600;margin-top:4px}
.stat.teal{background:linear-gradient(135deg,var(--teal),#2a9fd0)}
.stat.blue{background:linear-gradient(135deg,var(--blue),var(--blue-dark))}
.card{background:#fff;border-radius:5px;padding:6px 7px;border:1px solid var(--line)}
.card h3{font-size:6.5px;font-weight:600;margin-bottom:4px}
.row{display:flex;align-items:center;gap:4px;font-size:5px;padding:2.5px 0;border-bottom:1px solid var(--line);color:var(--ink)}
.row:last-child{border-bottom:0}
.row .dot{width:6px;height:6px;border-radius:50%;background:var(--blue-soft);border:1px solid var(--blue);flex:none}
.row .amt{margin-left:auto;font-weight:600}
.pos{color:var(--green)}.neg{color:var(--red)}.warn{color:var(--amber)}
.pair{display:flex;gap:6px}
.pair .card{flex:1}

/* ---------- phone ---------- */
.phone{position:absolute;width:150px;height:383px;border:3px solid var(--frame);border-radius:18px;background:var(--panel);overflow:hidden;display:flex;flex-direction:column}
.status{height:14px;display:flex;justify-content:space-between;align-items:center;padding:0 10px;font-size:5.5px;font-weight:600;color:#fff;background:var(--blue)}
.phead{background:var(--blue);color:#fff;padding:4px 10px 10px}
.phead h2{font-size:10px;font-weight:600}
.phead small{display:block;font-size:5.5px;opacity:.85;margin-top:2px}
.tabs{display:flex;gap:4px;margin:6px 8px 0}
.tab{flex:1;text-align:center;font-size:5.5px;padding:3px 0;border-radius:8px;background:#fff;border:1px solid var(--line);color:var(--muted)}
.tab.on{background:var(--blue);color:#fff;border-color:var(--blue)}
.pbody{flex:1;padding:7px 8px;display:flex;flex-direction:column;gap:6px}
.ptitle{font-size:7px;font-weight:600}
.big{font-size:9px;font-weight:600;color:var(--blue)}
.pnav{height:24px;background:#fff;border-top:1px solid var(--line);display:flex;justify-content:space-around;align-items:center}
.pnav i{width:8px;height:8px;border-radius:2px;border:1.2px solid var(--muted);display:block}
.pnav i.on{border-color:var(--blue);background:var(--blue-soft)}
.opt{display:flex;align-items:center;gap:5px;font-size:6px;background:#fff;border:1px solid var(--line);border-radius:5px;padding:5px 6px}
.opt i{width:7px;height:7px;border-radius:50%;border:1.2px solid var(--muted);display:block}
.opt.on{border-color:var(--blue)}
.opt.on i{border-color:var(--blue);background:radial-gradient(var(--blue) 40%,#fff 45%)}
.btns{display:flex;gap:5px;margin-top:auto}
.btn{flex:1;text-align:center;font-size:6px;font-weight:600;padding:5px 0;border-radius:10px;border:1px solid var(--blue);color:var(--blue);background:#fff}
.btn.fill{background:var(--blue);color:#fff}
.progress{height:3px;border-radius:2px;background:var(--line);overflow:hidden}
.progress span{display:block;height:100%;width:35%;background:var(--blue)}
.mini{transform:scale(.35);transform-origin:top left}

/* wide mobile app frame */
.phone.wide{width:207px;height:428px}
.acct{background:#fff;color:var(--ink);border-radius:6px;padding:6px 7px;margin-top:7px;font-size:5.5px}
.acct b{display:block;font-size:10px;color:var(--blue);margin-top:2px}
</style>
</head>
<body>

<!-- ===== Overview (flat) ===== -->
<section class="overview">
  <div class="desk" style="left:25px;top:120px">
    <aside class="side">
      <div class="brand"><i></i>Keyvale</div>
      <div class="search">Search</div>
      <div class="nav on">Dashboard</div><div class="nav">Properties</div><div class="nav">Tenants</div><div class="nav">Finances</div><div class="nav">Compliance</div><div class="nav">Maintenance</div><div class="nav">Reports</div><div class="nav">Settings</div>
      <div class="nav out">Log out</div>
    </aside>
    <div class="main">
      <div class="top"><h1>Dashboard</h1><div class="user"><i></i>Alex Reed</div></div>
      <div class="body">
        <div class="col left">
          <div class="stats"><div class="stat teal">Total income<b>£84,250.00</b></div><div class="stat blue">Outstanding<b>£12,480.00</b></div></div>
          <div class="card"><h3>General</h3>
            <div class="row"><span class="dot"></span>14 Elm Court – rent due<span class="amt">£950</span></div>
            <div class="row"><span class="dot"></span>Gas safety check booked<span class="amt warn">Pending</span></div>
            <div class="row"><span class="dot"></span>New tenancy signed<span class="amt pos">Done</span></div>
          </div>
          <div class="pair">
            <div class="card"><h3>Compliance</h3><div class="row"><span class="dot"></span>Overdue<span class="amt neg">3</span></div><div class="row"><span class="dot"></span>Due soon<span class="amt warn">5</span></div></div>
            <div class="card"><h3>Finances</h3><div class="row"><span class="dot"></span>Receivable<span class="amt pos">£8,200</span></div><div class="row"><span class="dot"></span>Payable<span class="amt neg">£4,280</span></div></div>
          </div>
        </div>
        <div class="col right">
          <div class="card"><h3>Activity</h3>
            <div class="row"><span class="dot"></span>Invoice sent</div>
            <div class="row"><span class="dot"></span>Repair logged</div>
            <div class="row"><span class="dot"></span>Inspection done</div>
            <div class="row"><span class="dot"></span>Deposit held</div>
          </div>
        </div>
      </div>
    </div>
  </div>

  <div class="abs" style="left:510px;top:150px;width:53px;height:134px"><div class="phone mini" style="position:relative">
    <div class="status"><span>9:41</span><span>●●●</span></div>
    <div class="phead"><h2>Dashboard</h2><div class="acct">Balance<b>£84,250.00</b></div></div>
    <div class="pbody"><div class="ptitle">General</div><div class="card"><div class="row"><span class="dot"></span>Rent due<span class="amt">£950</span></div><div class="row"><span class="dot"></span>Check booked</div></div></div>
    <div class="pnav"><i class="on"></i><i></i><i></i><i></i></div></div></div>
  <div class="abs" style="left:567px;top:130px;width:53px;height:134px"><div class="phone mini" style="position:relative">
    <div class="status"><span>9:41</span><span>●●●</span></div>
    <div class="phead"><h2>Finances</h2></div>
    <div class="pbody"><div class="card"><div class="row"><span class="dot"></span>Receivable<span class="amt pos">£8,200</span></div><div class="row"><span class="dot"></span>Payable<span class="amt neg">£4,280</span></div></div></div>
    <div class="pnav"><i></i><i class="on"></i><i></i><i></i></div></div></div>
  <div class="abs" style="left:624px;top:150px;width:53px;height:134px"><div class="phone mini" style="position:relative">
    <div class="status"><span>9:41</span><span>●●●</span></div>
    <div class="phead"><h2>Compliance</h2></div>
    <div class="pbody"><div class="opt on"><i></i>Yes</div><div class="opt"><i></i>No</div></div>
    <div class="pnav"><i></i><i></i><i class="on"></i><i></i></div></div></div>
  <div class="abs" style="left:681px;top:130px;width:53px;height:134px"><div class="phone mini" style="position:relative">
    <div class="status"><span>9:41</span><span>●●●</span></div>
    <div class="phead"><h2>Properties</h2></div>
    <div class="pbody"><div class="card"><div class="row"><span class="dot"></span>14 Elm Court</div><div class="row"><span class="dot"></span>2 Mill Lane</div></div></div>
    <div class="pnav"><i></i><i></i><i></i><i class="on"></i></div></div></div>
</section>

<!-- ===== Dashboard // Desktop ===== -->
<div class="label" style="left:25px;top:521px">Dashboard // Desktop App</div>
<div class="desk" style="left:25px;top:534px">
  <aside class="side">
    <div class="brand"><i></i>Keyvale</div>
    <div class="search">Search</div>
    <div class="nav on">Dashboard</div><div class="nav">Properties</div><div class="nav">Tenants</div><div class="nav">Finances</div><div class="nav">Compliance</div><div class="nav">Maintenance</div><div class="nav">Reports</div><div class="nav">Settings</div>
    <div class="nav out">Log out</div>
  </aside>
  <div class="main">
    <div class="top"><h1>Dashboard</h1><div class="user"><i></i>Alex Reed</div></div>
    <div class="body">
      <div class="col left">
        <div class="stats"><div class="stat teal">Total income<b>£84,250.00</b></div><div class="stat blue">Outstanding<b>£12,480.00</b></div></div>
        <div class="card"><h3>General</h3>
          <div class="row"><span class="dot"></span>14 Elm Court – rent due<span class="amt">£950</span></div>
          <div class="row"><span class="dot"></span>Gas safety check booked<span class="amt warn">Pending</span></div>
          <div class="row"><span class="dot"></span>New tenancy signed<span class="amt pos">Done</span></div>
        </div>
        <div class="pair">
          <div class="card"><h3>Compliance</h3><div class="row"><span class="dot"></span>Overdue<span class="amt neg">3</span></div><div class="row"><span class="dot"></span>Due soon<span class="amt warn">5</span></div></div>
          <div class="card"><h3>Finances</h3><div class="row"><span class="dot"></span>Receivable<span class="amt pos">£8,200</span></div><div class="row"><span class="dot"></span>Payable<span class="amt neg">£4,280</span></div></div>
        </div>
      </div>
      <div class="col right">
        <div class="card"><h3>Activity</h3>
          <div class="row"><span class="dot"></span>Invoice sent</div>
          <div class="row"><span class="dot"></span>Repair logged</div>
          <div class="row"><span class="dot"></span>Inspection done</div>
          <div class="row"><span class="dot"></span>Deposit held</div>
        </div>
      </div>
    </div>
  </div>
</div>

<!-- ===== Dashboard // Mobile ===== -->
<div class="label" style="left:528px;top:521px">Dashboard // Mobile App</div>
<div class="phone wide" style="left:528px;top:534px">
  <div class="status"><span>9:41</span><span>●●●</span></div>
  <div class="phead"><h2>Dashboard</h2><small>Good morning, Alex</small>
    <div class="acct">Total balance<b>£84,250.00</b></div></div>
  <div class="pbody">
    <div class="card"><h3>Notices</h3><div class="row"><span class="dot"></span>Please complete setup<span class="amt warn">!</span></div></div>
    <div class="ptitle">General</div>
    <div class="card">
      <div class="row"><span class="dot"></span>14 Elm Court – rent due<span class="amt">£950</span></div>
      <div class="row"><span class="dot"></span>Gas safety check booked</div>
      <div class="row"><span class="dot"></span>New tenancy signed<span class="amt pos">Done</span></div>
    </div>
    <div class="card"><h3>Compliance</h3><div class="row"><span class="dot"></span>Overdue<span class="amt neg">3</span></div><div class="row"><span class="dot"></span>Due soon<span class="amt warn">5</span></div><div class="row"><span class="dot"></span>Complete<span class="amt pos">18</span></div></div>
    <div class="card"><h3>Finances</h3><div class="row"><span class="dot"></span>Receivable<span class="amt pos">£8,200</span></div><div class="row"><span class="dot"></span>Payable<span class="amt neg">£4,280</span></div></div>
  </div>
  <div class="pnav"><i class="on"></i><i></i><i></i><i></i></div>
</div>

<!-- ===== Finances // AR ===== -->
<div class="label" style="left:25px;top:788px">Finances // AR</div>
<div class="phone" style="left:25px;top:800px">
  <div class="status"><span>9:41</span><span>●●●</span></div>
  <div class="phead"><h2>Finances</h2></div>
  <div class="tabs"><div class="tab on">Receivable</div><div class="tab">Payable</div></div>
  <div class="pbody">
    <div class="ptitle">Accounts Receivable</div>
    <div class="card"><h3>Income</h3><div class="big">£8,200.00</div>
      <div class="row"><span class="dot"></span>14 Elm Court<span class="amt pos">£950</span></div>
      <div class="row"><span class="dot"></span>2 Mill Lane<span class="amt pos">£1,100</span></div></div>
    <div class="card"><h3>Combined balance</h3><div class="big">£14,250.00</div></div>
  </div>
  <div class="pnav"><i></i><i class="on"></i><i></i><i></i></div>
</div>

<!-- ===== Finances // AP ===== -->
<div class="label" style="left:187px;top:788px">Finances // AP</div>
<div class="phone" style="left:187px;top:800px">
  <div class="status"><span>9:41</span><span>●●●</span></div>
  <div class="phead"><h2>Finances</h2></div>
  <div class="tabs"><div class="tab">Receivable</div><div class="tab on">Payable</div></div>
  <div class="pbody">
    <div class="ptitle">Accounts Payable</div>
    <div class="card"><h3>Outgoing</h3><div class="big">£4,280.00</div>
      <div class="row"><span class="dot"></span>Plumbing repair<span class="amt neg">£320</span></div>
      <div class="row"><span class="dot"></span>Cleaning<span class="amt neg">£140</span></div></div>
  </div>
  <div class="pnav"><i></i><i class="on"></i><i></i><i></i></div>
</div>

<!-- ===== Compliance // Question ===== -->
<div class="label" style="left:349px;top:788px">Compliance // Question</div>
<div class="phone" style="left:349px;top:800px">
  <div class="status"><span>9:41</span><span>●●●</span></div>
  <div class="phead"><h2>Compliance</h2><small>Legionella</small></div>
  <div class="pbody">
    <div class="progress"><span></span></div>
    <div class="ptitle">Question 1</div>
    <div style="font-size:6.5px">Is it required?</div>
    <div class="opt on"><i></i>Yes</div>
    <div class="opt"><i></i>No, risk assessed</div>
    <div class="opt"><i></i>Not sure, ask agent</div>
    <div class="btns"><div class="btn">Back</div><div class="btn fill">Next</div></div>
  </div>
  <div class="pnav"><i></i><i></i><i class="on"></i><i></i></div>
</div>

</body>
</html>
```